Etiketten-Design für Himbeer-Gin
Zielgruppe
GIN
Aufgabenstellung
Wir benötigen ein Etikett für unseren neuen Himbeere GIN, der Name des GINs lautet: KorvalaGIN und soll für folgende Flasche dargestellt werden: https://www.flakoria-beispiel.de/luma-flasche-500ml-schwarz-beschichtet-tqx41-karton-48stk.html
mit dem Etikett https://klebmarken-beispiel.de/anwendungen/fluoreszierende-etiketten/ Himbeerlastiges Design mit bestehendem Logo (WendelGIN) siehe Daten. Bei Fragen stehe ich gerne zur Verfügung!

```html
<!DOCTYPE html>
<html lang="de">
<head>
<meta charset="utf-8">
<title>KorvalaGIN Etikett</title>
<link rel="stylesheet" href="https://fonts.googleapis.com/css2?family=Cinzel:wght@600&family=Lato:wght@300;700&family=Saira+Condensed:wght@500;600&display=swap">
<style>
  :root {
    --backdrop: #161515;
    --label-deep: #b81f6e;
    --label-mid: #cc2f82;
    --label-light: #e262aa;
    --brand-silver: #ececec;
    --soft-pink: #f3a9d1;
    --dry-pink: #e58bbd;
    --variant-ink: #3a1d2c;
    --footer-white: #fbeaf3;
  }
  * { margin: 0; padding: 0; box-sizing: border-box; }
  html, body {
    width: 1161px;
    height: 1200px;
    overflow: hidden;
    background: var(--backdrop);
  }
  .label {
    position: absolute;
    left: 290px;
    top: 60px;
    width: 580px;
    height: 1080px;
    border-radius: 34px;
    background: linear-gradient(100deg, var(--label-deep) 0%, var(--label-mid) 55%, var(--label-light) 100%);
    overflow: hidden;
    color: var(--brand-silver);
  }
  .portrait {
    position: absolute;
    left: 50%;
    top: 12px;
    width: 118px;
    height: 185px;
    transform: translateX(-50%);
    border-radius: 50% 50% 46% 46%;
    background: radial-gradient(ellipse at 50% 45%, #e08fbd 0%, #c44a8c 70%, rgba(196,74,140,0) 100%);
  }
  .established {
    position: absolute;
    top: 116px;
    font-family: "Lato", sans-serif;
    font-weight: 300;
    font-size: 19px;
    letter-spacing: 1px;
    color: var(--soft-pink);
  }
  .established--label { left: 145px; }
  .established--year { right: 150px; }
  .brand-name {
    position: absolute;
    left: 0;
    right: 0;
    top: 170px;
    text-align: center;
    font-family: "Cinzel", serif;
    font-weight: 600;
    color: var(--brand-silver);
    line-height: 1;
  }
  .brand-name .brand-line { display: block; }
  .brand-name .brand-line--first { font-size: 84px; }
  .brand-name .brand-line--second { font-size: 160px; margin-top: 6px; }
  .region {
    position: absolute;
    left: 0; right: 0;
    top: 456px;
    text-align: center;
    font-family: "Lato", sans-serif;
    font-weight: 300;
    font-size: 38px;
    letter-spacing: 1px;
    color: var(--soft-pink);
  }
  .style {
    position: absolute;
    left: 0; right: 0;
    top: 508px;
    text-align: center;
    font-family: "Lato", sans-serif;
    font-weight: 700;
    font-size: 27px;
    letter-spacing: 1px;
    color: var(--dry-pink);
  }
  .variant {
    position: absolute;
    left: 0; right: 0;
    top: 574px;
    text-align: center;
    font-family: "Saira Condensed", sans-serif;
    font-weight: 600;
    font-size: 52px;
    letter-spacing: 7px;
    color: var(--variant-ink);
  }
  .reflection {
    position: absolute;
    left: 90px;
    top: 650px;
    width: 400px;
    height: 340px;
    background: linear-gradient(180deg, rgba(240,150,200,0.35) 0%, rgba(220,110,170,0.15) 60%, rgba(220,110,170,0) 100%);
    border-radius: 24px;
  }
  .specs {
    position: absolute;
    left: 88px;
    right: 78px;
    top: 1008px;
    display: flex;
    justify-content: space-between;
    font-family: "Saira Condensed", sans-serif;
    font-weight: 500;
    font-size: 29px;
    color: var(--footer-white);
  }
</style>
</head>
<body>
  <main class="label">
    <div class="portrait" role="img" aria-label="Portrait of the founder in pink monotone"></div>
    <span class="established established--label">ESTD.</span>
    <span class="established established--year">2019</span>
    <h1 class="brand-name">
      <span class="brand-line brand-line--first">Wendel</span>
      <span class="brand-line brand-line--second">GIN</span>
    </h1>
    <p class="region">SCHWÄBISCHER</p>
    <p class="style">DRY GIN</p>
    <h2 class="variant">KORVALA GIN</h2>
    <div class="reflection" role="img" aria-label="Faded mirrored repeat of the brand name and portrait"></div>
    <div class="specs">
      <span class="specs-volume">500 ml</span>
      <span class="specs-abv">40% vol</span>
    </div>
  </main>
</body>
</html>
```